Jardin Cobalte

I need à Web design call TazCoaching

With the following

Home page ( ACCUEIL )
PRODUCT ( JEUX EDUCATIFS )
About page ( QUI SUIS-JE )
Video page ( VIDEO )
Programme ( NOS FORMATIONS )
Books ( LIVRES )
Blog page ( PUBLIEZ ICI )
contact

f ...acebook
t..witter

The language need to be in french i send picture of me as a speaker
Updates

Target Market(s)

business owner and real estate investor

Industry/Entity Type

Call

Coding

Coded - Design and coding required

Number of Pages Required

5+ page

Font styles to use
Sans Serif
Script

Colors
a54499
aaaaaa
7f7f7f

Requirements
Must have
• my project should be same as the power point file and Word Press plug in
Nice to have
• any idea that you feel can improve conversion

```html
<!DOCTYPE html>
<html lang="fr">
<head>
<meta charset="utf-8">
<title>Lucien-Marc Daveau — Qui suis-je</title>
<link href="https://fonts.googleapis.com/css2?family=Roboto:wght@400;500;700&family=Roboto+Condensed:wght@400&family=Lora:ital,wght@1,400;1,700&display=swap" rel="stylesheet">
<style>
:root{
  --purple:#a54499;
  --pink:#d76ac9;
  --dark:#2b2b2b;
  --footer:#2d2d2d;
  --base:#222222;
  --accent:#e05ee0;
  --text:#3a3a3a;
  --muted:#aaaaaa;
  --grey:#7f7f7f;
  --white:#ffffff;
}
*{margin:0;padding:0;box-sizing:border-box}
html,body{width:1200px;height:1098px;overflow:hidden;background:var(--white);font-family:'Roboto',sans-serif}
.page{position:relative;width:1200px;height:1098px}
.abs{position:absolute}

.topbar{left:0;top:0;width:1200px;height:56px;background:var(--dark)}
.brand{left:245px;top:12px;font-family:'Roboto Condensed',sans-serif;font-size:26px;color:var(--white);letter-spacing:.2px;line-height:1;text-transform:uppercase}
.nav{left:493px;top:22px;display:flex;gap:7px;font-size:9px;color:var(--white);text-transform:uppercase}
.nav .on{color:var(--accent)}
.nav .gap{margin-left:4px}
.social-mini{left:924px;top:21px;display:flex;align-items:center;gap:5px}
.dot{width:8px;height:8px;border-radius:50%;background:var(--white)}
.sep{width:1px;height:10px;background:var(--white)}

.band{left:0;width:1200px;background:var(--purple)}
.band-top{top:56px;height:138px}
.band-bottom{top:606px;height:137px}
.pitch{font-family:'Lora',serif;font-style:italic;color:var(--white)}
.pitch .lead{font-size:15.5px;line-height:15px;letter-spacing:.5px}
.pitch .quote{font-weight:700;font-size:19px;line-height:18px;margin-top:14px;letter-spacing:.5px}

.optin{left:664px;width:301px}
.optin-head{height:52px;background:var(--dark);display:flex;align-items:center;padding-left:14px;gap:10px}
.arrow-circle{width:26px;height:26px;border-radius:50%;background:#f7e8ee;display:flex;align-items:center;justify-content:center}
.optin-title{font-size:11px;font-weight:500;color:var(--white);line-height:14px;text-transform:uppercase}
.optin-body{height:86px;background:var(--pink);padding:9px 15px 0 18px}
.labels{display:flex;font-size:9px;color:var(--white)}
.labels span{width:138px}
.fields{display:flex;gap:4px;margin-top:2px}
.field{width:131px;height:21px;background:var(--white);font-size:7px;color:#555;padding:6px 7px}
.btn{margin-top:7px;width:268px;height:25px;background:var(--dark);color:var(--white);font-size:10px;display:flex;align-items:center;justify-content:center;gap:6px}

.portrait{left:246px;top:228px;width:199px;height:243px;border:4px solid var(--purple);background:var(--white);padding:8px}
.portrait-fill{width:100%;height:100%;background:linear-gradient(160deg,#3d6a1e,#6a9a2c 45%,#c85b7a 70%,#2f4d16)}
.intro{left:489px;top:222px;width:465px}
.intro h1{font-size:20px;font-weight:500;color:#222;letter-spacing:.2px}
.intro p{font-size:8.8px;line-height:13.7px;color:var(--text);margin-top:14px}
.intro h1+p{margin-top:16px}

.tablet{left:242px;top:612px;width:70px;height:126px;border-radius:6px;background:#1e1e1e;padding:8px 6px}
.tablet-screen{width:100%;height:100%;background:linear-gradient(170deg,#5c3a2a,#a34545 55%,#d6a24a)}

.footer{left:0;top:743px;width:1200px;height:278px;background:var(--footer)}
.fnav{left:0;top:776px;width:1200px;display:flex;justify-content:center;gap:11px;font-size:9px;color:var(--muted);text-transform:uppercase}
.fnav .on{color:var(--accent)}
.col{top:823px;width:212px}
.col h3{font-size:12.5px;font-weight:400;color:var(--white);padding-bottom:10px;border-bottom:1px solid #bbb;letter-spacing:.2px}
.col ul{list-style:none;margin-top:10px}
.col li{font-size:7.4px;color:var(--muted);line-height:18.8px}
.circles{display:flex;gap:4px;margin:14px 0 0 6px}
.circles span{width:28px;height:28px;border-radius:50%;background:#7a7a7a}
.contact-h{margin-top:22px}
.card{display:flex;gap:8px;margin-top:11px;margin-left:6px}
.avatar{width:47px;height:40px;border:3px solid var(--white);background:linear-gradient(180deg,#6d4a3a,#2e2e40)}
.card div{font-size:9.5px;color:var(--white);line-height:16px;padding-top:3px}
.card small{font-size:8px;color:#ccc}

.base{left:0;top:1021px;width:1200px;height:77px;background:var(--base);text-align:center;color:#bbb}
.base .c{font-size:9px;margin-top:15px}
.base .l{font-size:7.5px;margin-top:9px}
</style>
</head>
<body>
<div class="page">
  <header class="abs topbar"></header>
  <div class="abs brand">Lucien-Marc Daveau</div>
  <nav class="abs nav">
    <span>Accueil</span><span>Jeux educatifs</span><span class="on">Qui suis-je</span><span>Video</span><span>Nos formations</span><span>Livres</span><span>Publiez ici</span><span class="gap">Contact</span>
  </nav>
  <div class="abs social-mini"><span class="dot"></span><span class="sep"></span><span class="dot"></span></div>

  <section class="abs band band-top"></section>
  <div class="abs pitch" style="left:251px;top:73px;width:400px">
    <div class="lead">Apprenez&nbsp; les secrets de cet entrepreneur qui réduit ces impôts de 95 % grâce à l’immobilier pour s’offrir une</div>
    <div class="quote">« vie de partage et de succès avec sa famille »</div>
  </div>
  <div class="abs optin" style="top:56px">
    <div class="optin-head">
      <span class="arrow-circle"><svg width="14" height="14" viewBox="0 0 14 14"><path d="M7 1v11M2.5 7.5 7 12l4.5-4.5" fill="none" stroke="#222" stroke-width="1.5"/></svg></span>
      <span class="optin-title">Recevez gratuitement nos articles et<br>nos videos de conseil en investissement</span>
    </div>
    <form class="optin-body">
      <div class="labels"><span>Votre prenom:</span><span>Votre email:</span></div>
      <div class="fields"><div class="field"></div><div class="field">(indiquez ici une adresse valide)</div></div>
      <div class="btn">Cliquez ici pour valider! <svg width="5" height="7" viewBox="0 0 5 7"><path d="M0 0l5 3.5L0 7z" fill="#fff"/></svg></div>
    </form>
  </div>

  <figure class="abs portrait"><div class="portrait-fill" role="img" aria-label="Portrait de Lucien-Marc Daveau, bras croisés devant un feuillage tropical"></div></figure>
  <article class="abs intro">
    <h1>INTRODUCTION OF LUCIEN</h1>
    <p>Lorem ipsum dolor sit amet, consectetur adipiscing elit. Proin sed libero fermentum, sagittis velit at, tincidunt ex. Fusce quis nulla tempor, auctor odio in, ornare nunc. Morbi sed imperdiet arcu. Quisque at viverra augue. Vestibulum placerat augue imperdiet, viverra dolor nec, rutrum nisl. Curabitur ac fringilla libero, ac sodales sem. Etiam a volutpat massa, ac elementum magna. Nam dignissim mi luctus sem consequat, vel convallis ante dignissim. Ut aliquam erat ante, vitae fermentum ligula tincidunt eu. Cras vestibulum lectus ipsum, ut efficitur quam hendrerit nec. Fusce mollis nulla velit, non accumsan sapien sodales ut. Aenean ante diam, eleifend semper orci et, tristique rutrum dui.</p>
    <p>Morbi eget nulla quis orci rhoncus tristique. Phasellus id mollis dolor, non feugiat urna. Praesent sagittis id elit non aliquet. Nullam velit eros, efficitur ac vehicula sed, malesuada a mi. Aliquam blandit velit purus, sed faucibus enim pretium eget. Nam metus turpis, dignissim a finibus quis, blandit nec dolor. Donec nisl arcu, facilisis id tortor non, rhoncus bibendum est. Donec eu laoreet eros.</p>
    <p>Curabitur facilisis eleifend posuere. Aliquam magna lacus, malesuada a ultrices et, tempus vel diam. Fusce non urna eu odio ullamcorper pulvinar sed aliquet purus. Vestibulum vitae mi purus. Sed id eros nisl. Praesent sagittis arcu at quam lobortis, euismod tempor ante rhoncus. Nunc cursus, massa ac dapibus commodo, nibh risus suscipit felis, id suscipit quam nisi sit amet purus.</p>
    <p>Phasellus tincidunt efficitur massa. Sed ut laoreet nisl. Etiam venenatis enim leo, nec maximus mauris eleifend non. Donec vitae nibh ex. In accumsan tellus id ipsum varius vestibulum. Quisque rhoncus dolor a lectus eleifend cursus. Pellentesque auctor purus vitae condimentum congue.</p>
  </article>

  <section class="abs band band-bottom"></section>
  <div class="abs tablet"><div class="tablet-screen" role="img" aria-label="Tablette montrant des joueurs autour d’un jeu de plateau"></div></div>
  <div class="abs pitch" style="left:325px;top:629px;width:320px">
    <div class="lead" style="font-size:15.5px">Découvrez la méthode de coaching en investissement immobilier de façon simple et efficace</div>
    <div class="quote" style="font-size:15px;line-height:16px;margin-top:12px">« le jeu Patrimoine 101 de Armand FERREL en français »</div>
  </div>
  <div class="abs optin" style="top:606px">
    <div class="optin-head">
      <span class="arrow-circle"><svg width="14" height="14" viewBox="0 0 14 14"><path d="M7 1v11M2.5 7.5 7 12l4.5-4.5" fill="none" stroke="#222" stroke-width="1.5"/></svg></span>
      <span class="optin-title">Recevez gratuitement nos articles et<br>nos videos de conseil en investissement</span>
    </div>
    <form class="optin-body">
      <div class="labels"><span>Votre prenom:</span><span>Votre email:</span></div>
      <div class="fields"><div class="field"></div><div class="field">(indiquez ici une adresse valide)</div></div>
      <div class="btn">Cliquez ici pour valider! <svg width="5" height="7" viewBox="0 0 5 7"><path d="M0 0l5 3.5L0 7z" fill="#fff"/></svg></div>
    </form>
  </div>

  <footer class="abs footer"></footer>
  <nav class="abs fnav">
    <span>Accueil</span><span>Jeux educatifs</span><span class="on">Qui suis-je</span><span>Video</span><span>Nos formations</span><span>Livres</span><span>Publiez ici</span><span>Contact</span>
  </nav>
  <div class="abs col" style="left:249px">
    <h3>TAZ DERNIÈRE&nbsp; PUBLICATION</h3>
    <ul>
      <li>Nunc accumsan diam quis&nbsp; varius ante pharetra.</li>
      <li>Aliquam a orci ornare, consequatpulvinar ante.</li>
      <li>Vestibulum ut risus at justo cu nec velit accumsan.</li>
      <li>Condimentum est ac, mollis purus.</li>
      <li>Nulla finibus ex sed metus maximus lacinia.</li>
    </ul>
  </div>
  <div class="abs col" style="left:481px">
    <h3>TAZ DERNIÈRE&nbsp; PUBLICATION</h3>
    <ul>
      <li>Lucien-Marc Publication</li>
      <li>Votre vision pour 12 a 36 mois</li>
      <li>Mon meilleur Outil pour investir sans apport et gagner</li>
      <li>Pourquoi une journée jeune Entrepreneur</li>
      <li>Comment&nbsp; passez de fauché à libre financièrement en mois</li>
      <li>de 60 mois</li>
      <li>Pourquoi un vrai investisseur est avant tout un Entrepreneur</li>
    </ul>
  </div>
  <div class="abs col" style="left:719px">
    <h3>CONNECT WITH ME</h3>
    <div class="circles"><span></span><span></span><span></span><span></span><span></span></div>
    <h3 class="contact-h">CONTACT ME</h3>
    <div class="card">
      <div class="avatar" role="img" aria-label="Petit portrait de Lucien-Marc Daveau"></div>
      <div>EMAIL:<br><small>lucien.daveau@tazcoaching.com</small></div>
    </div>
  </div>

  <div class="abs base">
    <div class="c">© 2016 Lucien-Marc DAVEAU</div>
    <div class="l">Terms of Use | Privacy Policy | Earnings Disclaimer</div>
  </div>
</div>
</body>
</html>
```